Out of town New Masters of Accounting

size of ad is 7” x 9.6”
please leave one inch on bottom for footer
We want to attract out of town students to join this master's in accounting program.
You DO NOT  have to use a picture of a person.
But if you do, it should be a  male with a white shirt and should not have long hair.(look like a young executive)
THE TEXT OF THE AD IS IN THE ATTACHMENTS
THE CAP LETTERS ARE THE INSTRUCTIONS

The age we are trying to attract is from 20-30 of ages.
- a clear ad .. the text should not take up the entire ad.. it should not be very crowded -
it should be an attractive ad that people would want to see and stand out
- the text very big and take up the entire ad

```html
<!DOCTYPE html>
<html lang="en">
<head>
<meta charset="utf-8">
<title>Master of Science in Accounting – Remote Program</title>
<link rel="stylesheet" href="https://fonts.googleapis.com/css2?family=Montserrat:wght@400;700;800&family=Signika:wght@400;500;600&display=swap">
<style>
  :root {
    --ink: #0f2226;
    --ink-deep: #0a1a1d;
    --amber: #f6a51d;
    --white: #ffffff;
    --slate: #3a4549;
    --bronze: #c8733a;
  }
  * { box-sizing: border-box; margin: 0; padding: 0; }
  html, body { width: 848px; height: 1200px; overflow: hidden; background: var(--ink); }
  .ad {
    position: relative; width: 848px; height: 1200px; overflow: hidden;
    background: var(--ink); font-family: "Signika", sans-serif; color: var(--white);
  }
  .hero-art { position: absolute; left: 0; top: 0; width: 848px; height: 640px; }
  .ranking-badge { position: absolute; left: 45px; top: 40px; width: 150px; height: 150px; }

  .headline { position: absolute; left: 42px; top: 508px; z-index: 2; }
  .headline .kicker { font-family: "Montserrat", sans-serif; font-size: 33px; color: var(--amber); font-weight: 400; line-height: 1.1; }
  .headline .degree { font-family: "Montserrat", sans-serif; font-size: 35px; font-weight: 400; letter-spacing: 0.5px; line-height: 1.3; }
  .headline .field { font-family: "Montserrat", sans-serif; font-size: 66px; font-weight: 800; color: var(--amber); line-height: 1; letter-spacing: 1px; }

  .program-strip {
    position: absolute; left: 42px; top: 666px; width: 738px; height: 42px;
    background: var(--amber); border-radius: 4px;
    font-size: 31px; font-weight: 500; color: var(--ink-deep);
    padding-left: 10px; line-height: 42px;
  }

  .benefits {
    position: absolute; left: 40px; top: 744px; width: 768px; height: 190px;
    background: var(--amber); border-radius: 32px;
    display: grid; grid-template-columns: 190px 155px 195px 228px;
    align-items: start; padding-top: 12px;
  }
  .benefit { text-align: center; color: var(--ink-deep); font-size: 21px; font-weight: 500; line-height: 1.28; }
  .benefit svg { display: block; margin: 0 auto 4px; height: 86px; }
  .benefit .figure { font-weight: 700; font-size: 23px; display: block; }

  .duration, .start { position: absolute; top: 958px; text-align: center; }
  .duration { left: 60px; width: 330px; }
  .start { left: 460px; width: 360px; }
  .lead { color: var(--amber); font-size: 31px; font-weight: 500; line-height: 1.1; }
  .big { font-family: "Montserrat", sans-serif; font-weight: 800; font-size: 44px; line-height: 1.15; }
  .note { color: var(--amber); font-size: 27px; font-weight: 500; letter-spacing: 0.5px; }
  .stars { margin-top: 6px; display: flex; justify-content: center; gap: 14px; }
  .divider { position: absolute; left: 433px; top: 965px; width: 4px; height: 112px; background: var(--amber); }

  .contact-bar {
    position: absolute; left: 83px; top: 1140px; width: 702px; height: 70px;
    background: var(--amber); border-radius: 18px 18px 0 0;
    text-align: center; font-size: 29px; color: var(--slate); font-weight: 500; padding-top: 8px;
  }
</style>
</head>
<body>
<main class="ad">

  <svg class="hero-art" viewBox="0 0 848 640">
    <defs>
      <linearGradient id="deskTone" x1="0" y1="0" x2="1" y2="1">
        <stop offset="0" stop-color="#d8c7ad"/>
        <stop offset="0.45" stop-color="#ece9e4"/>
        <stop offset="1" stop-color="#b9b3aa"/>
      </linearGradient>
    </defs>
    <g stroke="var(--amber)" stroke-width="10" stroke-linecap="round">
      <line x1="280" y1="105" x2="395" y2="-10"/>
      <line x1="225" y1="250" x2="355" y2="120"/>
      <line x1="205" y1="440" x2="270" y2="375"/>
      <line x1="610" y1="630" x2="860" y2="440"/>
      <line x1="660" y1="640" x2="860" y2="500"/>
    </g>
    <rect x="390" y="360" width="260" height="80" rx="40" fill="var(--amber)" transform="rotate(-45 520 400)"/>
    <path role="img" aria-label="Photo: overhead view of a desk with a laptop, tablet, phone and financial report papers being reviewed"
      d="M420 0 L848 0 L848 500 Q848 525 825 540 L620 625 Q570 640 555 600 L538 490 Q532 462 500 462 L320 460 Q268 456 266 405 L270 360 Q280 318 322 300 L342 262 Q326 160 360 110 Z"
      fill="url(#deskTone)" stroke="var(--white)" stroke-width="8" stroke-linejoin="round"/>
  </svg>

  <svg class="ranking-badge" viewBox="0 0 150 150" role="img" aria-label="Ranking badge">
    <circle cx="75" cy="75" r="62" fill="var(--amber)"/>
  </svg>

  <header class="headline">
    <p class="kicker">All New !!</p>
    <h1 class="degree">MASTER OF SCIENCE IN</h1>
    <p class="field">ACCOUNTING</p>
  </header>

  <p class="program-strip">Remote Program for Out of Town Students</p>

  <section class="benefits">
    <div class="benefit">
      <svg viewBox="0 0 100 90" aria-hidden="true">
        <circle cx="28" cy="22" r="12" fill="var(--ink-deep)"/>
        <circle cx="72" cy="22" r="12" fill="var(--ink-deep)"/>
        <path d="M8 70 q0-30 20-30 q20 0 20 30z M52 70 q0-30 20-30 q20 0 20 30z" fill="var(--ink-deep)"/>
        <circle cx="50" cy="42" r="20" fill="var(--amber)" stroke="var(--ink-deep)" stroke-width="7"/>
        <line x1="64" y1="56" x2="84" y2="80" stroke="var(--ink-deep)" stroke-width="9" stroke-linecap="round"/>
      </svg>
      KCS/Northgate<br>Alliance Job Place-<br>ment Advantage
    </div>
    <div class="benefit">
      <svg viewBox="0 0 100 90" aria-hidden="true">
        <rect x="12" y="60" width="12" height="26" fill="var(--ink-deep)"/>
        <rect x="30" y="50" width="12" height="36" fill="var(--ink-deep)"/>
        <rect x="48" y="40" width="12" height="46" fill="var(--ink-deep)"/>
        <rect x="66" y="30" width="12" height="56" fill="var(--ink-deep)"/>
        <polyline points="6,54 36,30 52,38 86,10" fill="none" stroke="var(--ink-deep)" stroke-width="6"/>
        <polygon points="94,2 76,6 90,20" fill="var(--ink-deep)"/>
      </svg>
      <span class="figure">96%</span>Placement<br>Rate
    </div>
    <div class="benefit">
      <svg viewBox="0 0 100 90" aria-hidden="true">
        <rect x="38" y="4" width="26" height="18" rx="4" fill="none" stroke="var(--ink-deep)" stroke-width="4"/>
        <circle cx="22" cy="38" r="9" fill="var(--ink-deep)"/>
        <circle cx="78" cy="38" r="9" fill="var(--ink-deep)"/>
        <path d="M10 70 q0-20 12-20 q12 0 12 20z M66 70 q0-20 12-20 q12 0 12 20z" fill="var(--ink-deep)"/>
        <rect x="30" y="58" width="40" height="8" fill="var(--ink-deep)"/>
        <rect x="46" y="66" width="8" height="20" fill="var(--ink-deep)"/>
      </svg>
      <span class="figure">8</span>Placement<br>Coordinators
    </div>
    <div class="benefit">
      <svg viewBox="0 0 120 90" aria-hidden="true">
        <polygon points="2,30 22,18 30,58 12,66" fill="var(--ink-deep)"/>
        <polygon points="118,30 98,18 90,58 108,66" fill="var(--ink-deep)"/>
        <path d="M28 28 l28-8 l30 4 l8 26 l-30 24 q-6 4-12 0 l-22-16z" fill="var(--ink-deep)"/>
        <path d="M50 34 l18-4 l20 18" fill="none" stroke="var(--amber)" stroke-width="4"/>
      </svg>
      Decades of<br>Relationships<br>with 100’s of firm
    </div>
  </section>

  <section class="duration">
    <p class="lead">A masters in only</p>
    <p class="big">15 Months</p>
    <div class="stars" aria-hidden="true">
      <svg width="56" height="54" viewBox="0 0 56 54"><polygon points="28,2 35,20 54,20 39,32 44,51 28,40 12,51 17,32 2,20 21,20" fill="var(--bronze)"/></svg>
      <svg width="56" height="54" viewBox="0 0 56 54"><polygon points="28,2 35,20 54,20 39,32 44,51 28,40 12,51 17,32 2,20 21,20" fill="var(--bronze)"/></svg>
      <svg width="56" height="54" viewBox="0 0 56 54"><polygon points="28,2 35,20 54,20 39,32 44,51 28,40 12,51 17,32 2,20 21,20" fill="var(--bronze)"/></svg>
    </div>
  </section>

  <div class="divider"></div>

  <section class="start">
    <p class="lead">Beginning from</p>
    <p class="big">AUGUST 17</p>
    <p class="note">NEW LOWER PRICES</p>
  </section>

  <footer class="contact-bar">Contact Info to Go here</footer>
</main>
</body>
</html>
```